VELVET MEADOW TOPICAL BOX W LABEL

This one will be a new design for me, so I may need to feel some things out.
My idea is to have some/ half iridescent, with white (top portion) and iridescent stamped logo
I googled my idea and found some pictures to help explain the style
Maybe an iridescent or white part may also be a palm tree ?
The name of the topical is
VELVET MEADOW
I'm not sure how to design the name on the front, but i dont expect it like the Fern Glow
The warnings and such are all the same from the other topicals. I will update the ingredients mostly and any other variable parts.

```html
<!DOCTYPE html>
<html lang="en">
<head>
<meta charset="UTF-8">
<title>Velvet Meadow Topical Box</title>
<link href="https://fonts.googleapis.com/css2?family=Big+Shoulders+Display:wght@700&family=Poppins:wght@400;500&display=swap" rel="stylesheet">
<style>
  :root {
    --page-bg: #f1f0ee;
    --title-orange: #ee5a26;
    --ink: #1f1f1f;
    --white: #ffffff;
    --warn-red: #e0262b;
    --iri-peach: #f9dcc6;
    --iri-pink: #f4c0cf;
    --iri-lilac: #d9cde6;
    --iri-sky: #c7e2f3;
    --iri-lemon: #f3ecc8;
  }
  * { margin: 0; padding: 0; box-sizing: border-box; }
  html, body {
    width: 1200px; height: 1200px; overflow: hidden;
    background: var(--page-bg);
  }
  .box-flat {
    position: absolute; left: 110px; top: 260px;
    display: flex; gap: 0;
    box-shadow: 0 20px 50px rgba(0,0,0,0.12);
  }
  .panel {
    position: relative; height: 680px; overflow: hidden;
  }
  .panel--front {
    width: 560px;
    background: linear-gradient(135deg, var(--iri-lemon) 0%, var(--iri-peach) 25%, var(--iri-pink) 55%, var(--iri-lilac) 85%);
  }
  .panel--side {
    width: 420px;
    background: linear-gradient(160deg, var(--iri-lilac) 0%, var(--iri-sky) 35%, var(--iri-pink) 70%, var(--iri-lilac) 100%);
    border-left: 1px solid rgba(0,0,0,0.08);
  }
  .palm-art {
    position: absolute; left: 0; top: 160px; width: 560px; height: 520px;
  }
  .product-name {
    position: absolute; left: 0; right: 0; top: 60px;
    font-family: "Big Shoulders Display", "Arial Narrow", sans-serif;
    font-weight: 700; color: var(--title-orange);
    font-size: 150px; line-height: 0.95; text-align: center;
    letter-spacing: 2px;
  }
  .dome {
    position: absolute; left: 0; bottom: 0; width: 560px; height: 300px;
  }
  .product-type {
    position: absolute; left: 0; right: 0; top: 480px;
    font-family: "Poppins", sans-serif; font-size: 34px; color: var(--ink);
    text-align: center;
  }
  .net-weight {
    position: absolute; left: 70px; bottom: 40px;
    font-family: "Poppins", sans-serif; font-size: 32px; color: var(--ink);
  }
  .warning-badge {
    position: absolute; right: 40px; bottom: 26px; width: 96px; height: 86px;
  }
  .side-palm {
    position: absolute; right: 0; top: 260px; width: 120px; height: 300px;
  }
  .description {
    position: absolute; left: 50px; right: 40px; top: 170px;
    font-family: "Poppins", sans-serif; font-size: 25px; line-height: 1.5;
    color: var(--ink); text-align: justify; hyphens: none;
  }
  .description em { font-style: italic; }
</style>
</head>
<body>
  <div class="box-flat">
    <section class="panel panel--front">
      <svg class="palm-art" role="img" aria-label="White palm tree silhouettes" viewBox="0 0 560 520">
        <defs>
          <radialGradient id="palmGlow" cx="0.6" cy="0.4" r="0.6">
            <stop offset="0" stop-color="#ffffff" stop-opacity="0.75"/>
            <stop offset="1" stop-color="#ffffff" stop-opacity="0"/>
          </radialGradient>
        </defs>
        <rect width="560" height="520" fill="url(#palmGlow)"/>
      </svg>
      <h1 class="product-name">VELVET<br>MEADOW</h1>
      <svg class="dome" viewBox="0 0 560 300" aria-hidden="true">
        <path d="M0 300 L0 150 Q280 -40 560 150 L560 300 Z" fill="var(--white)"/>
      </svg>
      <p class="product-type">Topical</p>
      <p class="net-weight">Net Wt. 2oz (56g)</p>
      <svg class="warning-badge" viewBox="0 0 96 86" aria-label="Regulatory warning mark">
        <path d="M48 6 L90 80 L6 80 Z" fill="var(--white)" stroke="var(--warn-red)" stroke-width="6" stroke-linejoin="round"/>
      </svg>
    </section>
    <section class="panel panel--side">
      <svg class="side-palm" role="img" aria-label="Faint white palm frond" viewBox="0 0 120 300">
        <defs>
          <linearGradient id="sideGlow" x1="0" x2="1">
            <stop offset="0" stop-color="#ffffff" stop-opacity="0"/>
            <stop offset="1" stop-color="#ffffff" stop-opacity="0.6"/>
          </linearGradient>
        </defs>
        <rect width="120" height="300" fill="url(#sideGlow)"/>
      </svg>
      <p class="description">Velvet Meadow delivers a downpour of soothing relief complemented by its signature Velvet Meadow oil blend (Moroccan Argan, Coconut, Tahitian Vanilla, and a squeeze of <em>Orange Essence) to boost feelings of relaxation.</em></p>
    </section>
  </div>
</body>
</html>
```